Wine Label for a wine from Tuscany, Italy

We need a wine label for a white and red wine, can be the same label or can be somewhat differentiated with any variation you feel would be good.. These two wines come from Tuscany, Italy. Wine labels from Tuscany Italy tend to be traditional. We are open to traditional looking labels but also more modern, eye catching too. We want to convey a sense of elegance, importance, great wine. I am attaching some examples of labels we like from Tuscany, also a label that was designed for us recently by one of you, which we LOVE. No wine glasses, wine bottles or grapes featured on the label please. We tend to like the white background. No blue please.

Target Market(s)

More women than men purchase wine, but it needs to appeal to both sexes.

Requirements
Must have
• Wine Name: Casa Morel or Casa morel
• Type/Varletal: Rosso Toscano (White is Vermentino)
• Vintage (year): 2018
• That is all the text we want on the label, thanks
Nice to have
• Clean, something that makes someone want to grab this wine bottle off the shelf!
Should not have
• Images of Wine glass, wine bottles, grapes
• Do not use the color blue please.

```html
<!DOCTYPE html>
<html lang="it">
<head>
<meta charset="utf-8">
<title>Casa Morel – Rosso Toscano 2018</title>
<link rel="stylesheet" href="https://fonts.googleapis.com/css2?family=Cormorant+Garamond:wght@400;500&display=swap">
<style>
  :root {
    --backdrop: #000000;
    --label-paper: #faf9f6;
    --ink: #0b0b0b;
    --rosso: #c8103f;
  }
  html, body {
    margin: 0;
    padding: 0;
    width: 1200px;
    height: 912px;
    overflow: hidden;
    background: var(--backdrop);
  }
  .canvas {
    position: relative;
    width: 1200px;
    height: 912px;
    background: var(--backdrop);
  }
  .wine-label {
    position: absolute;
    left: 273px;
    top: 130px;
    width: 653px;
    height: 653px;
    background: var(--label-paper);
    font-family: "Cormorant Garamond", Georgia, serif;
    text-align: center;
  }
  .wine-name {
    position: absolute;
    left: 0;
    right: 0;
    top: 205px;
    margin: 0;
    font-weight: 400;
    font-size: 82px;
    line-height: 1;
    letter-spacing: 3px;
    color: var(--ink);
  }
  .varietal {
    position: absolute;
    left: 0;
    right: 0;
    top: 487px;
    margin: 0;
    font-weight: 400;
    font-size: 52px;
    line-height: 1;
    letter-spacing: 5px;
    color: var(--rosso);
  }
  .vintage {
    position: absolute;
    left: 0;
    right: 0;
    top: 596px;
    margin: 0;
    font-weight: 500;
    font-size: 22px;
    line-height: 1;
    letter-spacing: 7px;
    color: var(--ink);
  }
</style>
</head>
<body>
  <main class="canvas">
    <section class="wine-label">
      <h1 class="wine-name">CASA MOREL</h1>
      <p class="varietal">ROSSO TOSCANO</p>
      <p class="vintage">~2018~</p>
    </section>
  </main>
</body>
</html>
```